Investment website design - investing in mutual funds

I need a design of a website (only homepage for now) dedicated to investment in mutual funds. Attached is a mock up with all the elements the homepage design should contain. The homepage should contain a logo in the upper left corner, the domain the website will run on is www.perovalstrinka.cz , in the upper right corner there should be 2 buttons or links SIGN UP / SIGN IN. The bottom of the homepage should contain links to ABOUT US, FAQ, PRIVACY POLICY, CONTACT US.
Now the main elements on the homepage
1) Video that will explain how the investment works exactly, under this video we will have 3 illustrated icons like the ones attached (see 2nd attachement) that will show the potential investor what exactly they could get when investing with us (education for kids, happy life after they retire, regular monthly payment for the rest of their life).
2) On the right side next to the video we will have a calculator where a potential investor can play with the numbers, the investor can fill in the MONTHLY PAYMENT that he wants to invest regularly every month, the time frame of the investment - for how long he wants to invest. Once the potential investor selects those 2 variables we will calculate for him 2 options - either he can get a ONE TIME PAYOUT once he reaches his investment horizon or he can get a regular monthly payment for the rest of his life. Under the laculator there will be a button 'I want to invest ->'. The functionality of the calculator should be similar to the calculator that can be found here http://www.brodavbank.cz/brodav-podilove-fondy/ and https://felbo.cz/.
The design should look similar to https://felbo.cz/ (font, colors, logo). We prefer white background in the area where we have the video and calculator. We also like the design of www.tarvupo.com. Let me know if you have any questions.

```html
<!DOCTYPE html>
<html lang="en">
<head>
<meta charset="utf-8">
<title>Mutual Funds Investment – Home</title>
<link rel="stylesheet" href="https://fonts.googleapis.com/css2?family=Roboto:wght@400;500;700&family=Ubuntu:wght@400;500&display=swap">
<style>
  :root {
    --teal-top: #23c4de;
    --teal-bottom: #74e8d9;
    --teal-accent: #3db3c2;
    --teal-shadow: #3aa9bd;
    --orange: #e5573a;
    --page-grey: #f3f3f3;
    --card-white: #ffffff;
    --ink: #2a2a2a;
    --muted: #7a7a7a;
    --line: #d6d6d6;
    --track: #cfcfcf;
    --video-dark: #1a1a1a;
  }
  * { box-sizing: border-box; margin: 0; padding: 0; }
  html, body { width: 1200px; height: 857px; overflow: hidden; }
  body {
    position: relative;
    background: var(--page-grey);
    font-family: "Roboto", Arial, sans-serif;
    color: var(--ink);
  }
  .hero {
    position: absolute; left: 0; top: 0; width: 838px; height: 857px;
    background: linear-gradient(160deg, var(--teal-top) 0%, #3fd2dc 55%, var(--teal-bottom) 100%);
  }
  .brand {
    position: absolute; left: 110px; top: 24px;
    font-family: "Ubuntu", Arial, sans-serif; font-weight: 500;
    font-size: 24px; color: #fff;
  }
  .auth { position: absolute; left: 906px; top: 26px; display: flex; gap: 4px; }
  .auth-btn {
    display: flex; align-items: center; justify-content: center; gap: 6px;
    width: 89px; height: 34px; color: #fff; text-decoration: none;
    font-size: 15px; font-weight: 500;
  }
  .auth-btn svg { width: 14px; height: 14px; }
  .auth-btn--in { background: var(--orange); }
  .auth-btn--up { background: var(--teal-accent); }

  .section-title {
    position: absolute; left: 111px; top: 152px;
    font-size: 27px; font-weight: 700; color: #fff;
  }
  .video {
    position: absolute; left: 111px; top: 205px; width: 531px; height: 324px;
    background: radial-gradient(ellipse at 40% 40%, #3a3a3a 0%, var(--video-dark) 70%);
  }
  .video-play {
    position: absolute; left: 350px; top: 347px; width: 55px; height: 39px;
    background: #fff; border-radius: 9px; display: flex; align-items: center; justify-content: center;
  }

  .benefits { position: absolute; left: 111px; top: 555px; display: flex; gap: 25px; }
  .benefit { width: 160px; text-align: center; }
  .benefit-badge { position: relative; width: 160px; height: 160px; }
  .benefit-badge svg { position: absolute; left: 0; top: 0; }
  .benefit-label { margin-top: 20px; font-size: 15.5px; font-weight: 500; color: #111; }

  .calculator {
    position: absolute; left: 684px; top: 183px; width: 404px; height: 469px;
    background: var(--card-white);
    clip-path: polygon(0 0, 364px 0, 404px 40px, 404px 100%, 0 100%);
  }
  .calculator-fold {
    position: absolute; left: 1048px; top: 183px; width: 40px; height: 40px;
    background: linear-gradient(225deg, transparent 50%, #d3d3d3 50%);
  }
  .calculator-title {
    position: absolute; left: 26px; top: 22px; font-size: 27px; font-weight: 700; color: #2b2b2b;
  }
  .field {
    position: absolute; left: 26px; width: 353px; height: 46px;
    border: 1px solid var(--line); padding: 0 16px;
    display: flex; align-items: center; font-size: 13.5px; color: var(--muted);
  }
  .field--monthly-investment { top: 72px; }
  .field--one-time { top: 221px; }
  .field--monthly-payment { top: 324px; }
  .slider-label {
    position: absolute; left: 25px; top: 133px; font-size: 15px; font-weight: 500; color: #222;
  }
  .slider-track {
    position: absolute; left: 26px; top: 168px; width: 353px; height: 12px; background: var(--track);
  }
  .slider-fill { position: absolute; left: 0; top: 0; width: 83px; height: 12px; background: var(--teal-accent); }
  .slider-knob {
    position: absolute; left: 72px; top: -5px; width: 22px; height: 22px; border-radius: 50%;
    background: var(--orange); border: 2px solid #fff; box-shadow: 0 0 0 1px rgba(0,0,0,.08);
  }
  .slider-knob::after {
    content: ""; position: absolute; left: 6px; top: 6px; width: 6px; height: 6px; border-radius: 50%; background: #fff;
  }
  .slider-min, .slider-max { position: absolute; top: 191px; font-size: 14px; color: #444; }
  .slider-min { left: 26px; font-size: 15px; }
  .slider-max { right: 25px; }
  .divider { position: absolute; left: 26px; top: 295px; width: 353px; height: 1px; background: #e6e6e6; }
  .divider-or {
    position: absolute; left: 187px; top: 280px; width: 31px; height: 31px; border-radius: 50%;
    background: #fff; border: 1px solid #e3e3e3; display: flex; align-items: center; justify-content: center;
    font-size: 11px; color: #555;
  }
  .invest-btn {
    position: absolute; left: 26px; top: 396px; width: 353px; height: 46px; background: var(--orange);
    color: #fff; font-size: 15.5px; font-weight: 700;
    display: flex; align-items: center; justify-content: center; gap: 7px;
  }
  .footer-nav {
    position: absolute; right: 112px; top: 824px; font-size: 12px; color: #333;
  }
  .footer-nav a { color: #333; text-decoration: none; }
  .footer-nav .sep { margin: 0 6px; }
</style>
</head>
<body>
  <div class="hero"></div>

  <div class="brand">Company Logo</div>

  <nav class="auth">
    <a class="auth-btn auth-btn--in" href="#">
      <svg viewBox="0 0 14 14" fill="none" stroke="#fff" stroke-width="1.4"><path d="M5 2h7v10H5"/><path d="M1 7h7M5.5 4.5 8 7l-2.5 2.5"/></svg>
      Sign In
    </a>
    <a class="auth-btn auth-btn--up" href="#">
      <svg viewBox="0 0 14 14" fill="none" stroke="#fff" stroke-width="1.4"><path d="M6 2H1.5v10.5H12V8"/><path d="M11 1.5 13 3.5 7 9.5H5v-2z"/></svg>
      Sign Up
    </a>
  </nav>

  <h1 class="section-title">Video About Our Product</h1>
  <div class="video" role="img" aria-label="Video thumbnail: 'Mutual Funds' title with a hand drawing a dollar sign"></div>
  <div class="video-play">
    <svg width="16" height="18" viewBox="0 0 16 18"><path d="M2 1l13 8-13 8z" fill="#222"/></svg>
  </div>

  <section class="benefits">
    <div class="benefit">
      <div class="benefit-badge">
        <svg width="160" height="160" viewBox="0 0 160 160">
          <path d="M95 6c30 6 65 70 58 110-5 30-40 38-75 36C40 150 6 130 10 100 14 65 60 0 95 6z" fill="var(--teal-shadow)"/>
          <path d="M86 2c30 6 60 72 53 112-5 28-38 35-72 33C33 145 4 125 8 96 12 62 54-4 86 2z" fill="#fff"/>
          <ellipse cx="78" cy="90" rx="46" ry="34" fill="#f0a93a" opacity=".9" role="img" aria-label="Illustration: graduation cap on a stack of books"/>
        </svg>
      </div>
      <p class="benefit-label">Education for Kids</p>
    </div>
    <div class="benefit">
      <div class="benefit-badge">
        <svg width="160" height="160" viewBox="0 0 160 160">
          <path d="M95 6c30 6 65 70 58 110-5 30-40 38-75 36C40 150 6 130 10 100 14 65 60 0 95 6z" fill="var(--teal-shadow)"/>
          <path d="M86 2c30 6 60 72 53 112-5 28-38 35-72 33C33 145 4 125 8 96 12 62 54-4 86 2z" fill="#fff"/>
          <ellipse cx="78" cy="88" rx="44" ry="36" fill="#e8674a" opacity=".85" role="img" aria-label="Illustration: cuckoo clock releasing coins"/>
        </svg>
      </div>
      <p class="benefit-label">Passive Income</p>
    </div>
    <div class="benefit">
      <div class="benefit-badge">
        <svg width="160" height="160" viewBox="0 0 160 160">
          <path d="M95 6c30 6 65 70 58 110-5 30-40 38-75 36C40 150 6 130 10 100 14 65 60 0 95 6z" fill="var(--teal-shadow)"/>
          <path d="M86 2c30 6 60 72 53 112-5 28-38 35-72 33C33 145 4 125 8 96 12 62 54-4 86 2z" fill="#fff"/>
          <ellipse cx="80" cy="92" rx="46" ry="32" fill="#f2a53a" opacity=".9" role="img" aria-label="Illustration: person relaxing in a bean bag chair"/>
        </svg>
      </div>
      <p class="benefit-label">Happy Retirement</p>
    </div>
  </section>

  <section class="calculator">
    <h2 class="calculator-title">Our Online Calculator</h2>
    <div class="field field--monthly-investment">Regular monthly investment:</div>
    <div class="slider-label">Length of investment</div>
    <div class="slider-track">
      <div class="slider-fill"></div>
      <div class="slider-knob"></div>
    </div>
    <span class="slider-min">0</span>
    <span class="slider-max">30 Years</span>
    <div class="field field--one-time">One time payout:</div>
    <div class="divider"></div>
    <div class="divider-or">OR</div>
    <div class="field field--monthly-payment">Mothly payment:</div>
    <div class="invest-btn">I want to invest
      <svg width="7" height="9" viewBox="0 0 7 9"><path d="M0 0l7 4.5L0 9z" fill="#fff"/></svg>
    </div>
  </section>
  <div class="calculator-fold"></div>

  <footer class="footer-nav">
    <a href="#">About Us</a><span class="sep">|</span><a href="#">FAQ</a><span class="sep">|</span><a href="#">Privacy Policy</a><span class="sep">|</span><a href="#">Contact</a>
  </footer>
</body>
</html>
```